Business Card of PebbleFinch
PebbleFinch
Bright & Fun-filled
Daniel Osei, CFA
President
412 Whitmore Suite 208
Irvine, CA 92655
daniel@pebblefinch.example
pebblefinch.example

```html
<!DOCTYPE html>
<html lang="en">
<head>
<meta charset="utf-8">
<title>PebbleFinch Stationery</title>
<link href="https://fonts.googleapis.com/css2?family=Roboto:wght@400;700&display=swap" rel="stylesheet">
<style>
  :root{
    --backdrop:#8e8e8e;
    --paper:#ffffff;
    --orange:#f6ae24;
    --red:#e0262b;
    --ink:#555555;
    --faint:#fbefd6;
  }
  html,body{margin:0;padding:0;overflow:hidden;}
  body{width:1200px;height:949px;background:var(--backdrop);position:relative;font-family:"Roboto",Arial,sans-serif;}
  .item{position:absolute;box-shadow:0 2px 6px rgba(0,0,0,.25);}
  .item svg{position:absolute;left:0;top:0;}
  .wordmark{position:absolute;font-family:"Roboto",Arial,sans-serif;font-weight:700;color:var(--red);white-space:nowrap;display:flex;align-items:center;gap:.3em;letter-spacing:-.02em;line-height:1;}
  .wordmark .dot{display:inline-block;width:.55em;height:.55em;border-radius:50%;background:var(--orange);}
  .small-text{position:absolute;color:var(--ink);font-size:6px;line-height:1.35;}
  .brand-top{left:862px;top:44px;font-size:40px;}
  .letterhead{left:41px;top:97px;width:436px;height:600px;background:var(--paper);}
  .letterhead .wordmark{left:50%;transform:translateX(-50%);top:36px;font-size:18px;}
  .letterhead .faint-mark{position:absolute;left:0;right:0;text-align:center;top:262px;font-size:62px;font-weight:700;color:var(--faint);line-height:1;}
  .letterhead .sender{right:24px;top:34px;text-align:left;}
  .sleeve{left:538px;top:236px;width:308px;height:290px;background:var(--paper);}
  .sleeve .wordmark{left:50%;transform:translateX(-50%);top:130px;font-size:22px;}
  .disc{left:813px;top:230px;width:298px;height:298px;border-radius:50%;overflow:hidden;background:var(--paper);}
  .disc .wordmark{left:140px;top:86px;font-size:14px;}
  .envelope{left:610px;top:610px;width:539px;height:270px;background:var(--paper);}
  .envelope .wordmark{left:50%;transform:translateX(-50%);top:130px;font-size:28px;}
  .card{top:774px;width:247px;height:134px;background:var(--paper);}
  .card-back{left:36px;}
  .card-front{left:336px;}
  .card-back .wordmark{left:148px;top:28px;font-size:10px;}
  .card-back .contact{left:12px;top:16px;}
  .card-back .contact strong{font-size:7px;}
  .card-front .wordmark{left:50%;transform:translateX(-50%);top:46px;font-size:16px;}
  .card-front .site{left:0;right:0;top:74px;text-align:center;font-size:6px;}
</style>
</head>
<body>

<div class="wordmark brand-top">PebbleFinch</div>

<section class="item letterhead">
  <svg width="436" height="600" viewBox="0 0 436 600">
    <path d="M0,62 Q70,18 160,0 L190,0 Q90,22 0,78 Z" fill="var(--red)"/>
    <path d="M0,560 Q230,600 436,478 L436,600 L0,600 Z" fill="var(--orange)"/>
    <path d="M170,565 Q330,548 436,462 L436,480 Q330,560 170,565 Z" fill="var(--red)"/>
  </svg>
  <div class="faint-mark">PebbleFinch</div>
  <div class="wordmark"><span class="dot"></span>PebbleFinch</div>
  <div class="small-text sender">412 Whitmore Suite 208<br>Irvine, CA 92655</div>
</section>

<section class="item sleeve">
  <svg width="308" height="290" viewBox="0 0 308 290">
    <path d="M150,0 Q250,12 308,52 L308,74 Q240,24 120,0 Z" fill="var(--red)"/>
    <circle cx="308" cy="52" r="30" fill="var(--backdrop)"/>
    <path d="M0,260 Q160,272 308,200 L308,290 L0,290 Z" fill="var(--orange)"/>
    <path d="M0,232 Q120,262 220,238 Q120,270 0,250 Z" fill="var(--red)"/>
  </svg>
  <div class="wordmark"><span class="dot"></span>PebbleFinch</div>
</section>

<section class="item disc">
  <svg width="298" height="298" viewBox="0 0 298 298">
    <path d="M150,0 Q260,20 298,120 L298,140 Q250,40 120,0 Z" fill="var(--red)"/>
    <path d="M0,250 Q180,270 298,150 L298,298 L0,298 Z" fill="var(--orange)"/>
    <path d="M0,215 Q120,255 230,220 Q120,270 0,232 Z" fill="var(--red)"/>
    <circle cx="149" cy="149" r="30" fill="var(--backdrop)"/>
  </svg>
  <div class="wordmark"><span class="dot"></span>PebbleFinch</div>
</section>

<section class="item envelope">
  <svg width="539" height="270" viewBox="0 0 539 270">
    <path d="M0,0 L539,0 L539,28 Q300,30 0,108 Z" fill="var(--orange)"/>
    <path d="M0,108 Q300,30 539,28 L539,36 Q280,44 20,104 Z" fill="var(--red)"/>
    <path d="M0,270 L0,258 Q280,262 539,172 L539,270 Z" fill="var(--orange)"/>
    <path d="M0,262 Q250,256 539,165 L539,176 Q270,262 0,262 Z" fill="var(--red)"/>
  </svg>
  <div class="wordmark"><span class="dot"></span>PebbleFinch</div>
</section>

<section class="item card card-back">
  <svg width="247" height="134" viewBox="0 0 247 134">
    <path d="M0,118 Q130,125 247,78 L247,134 L0,134 Z" fill="var(--orange)"/>
    <path d="M120,116 Q200,106 247,70 L247,78 Q200,114 120,116 Z" fill="var(--red)"/>
  </svg>
  <div class="small-text contact">
    <strong>Daniel Osei, CFA</strong><br>President<br><br>
    412 Whitmore Suite 208<br>Irvine, CA 92655<br>
    Tel (949) 555-0142<br>daniel@pebblefinch.example<br>pebblefinch.example
  </div>
  <div class="wordmark"><span class="dot"></span>PebbleFinch</div>
</section>

<section class="item card card-front">
  <svg width="247" height="134" viewBox="0 0 247 134">
    <path d="M0,118 Q130,125 247,78 L247,134 L0,134 Z" fill="var(--orange)"/>
    <path d="M120,116 Q200,106 247,70 L247,78 Q200,114 120,116 Z" fill="var(--red)"/>
  </svg>
  <div class="wordmark"><span class="dot"></span>PebbleFinch</div>
  <div class="small-text site">pebblefinch.example</div>
</section>

</body>
</html>
```